Website for Life Strategies business

We need a website to present our video, audio and print content to subcribers at Vivid Horizon Mentors. We will offer a team of coaches who can help people breakthrough the barriers that keep them from reaching their physical, spiritual, financial, leadership and relationship goals.

Target Market(s)

Anyone who needs help with strategies to take their life to a new level of success.

Industry/Entity Type

Life Coaching

Logo Text

Vivid Horizon Mentors

Number of Pages Required

5+ page

Colors

Designer to choose colors to be used in the design.

Requirements
Must have
• The ability to present content as a package that includes Word Documents, videos and audio content as well as to be able to display books for sale. Each week their would be a new package for subscribers to access. It should provide the ability for subscribers to comment on the material and share how their lives were changed by the content. Should also include a shop page to offer merchandise for sale.
Nice to have
• Not sure
Should not have
• Not sure

```html
<!DOCTYPE html>
<html lang="en">
<head>
<meta charset="utf-8">
<title>Vivid Horizon Mentors</title>
<link href="https://fonts.googleapis.com/css2?family=Titillium+Web:wght@400;600;700&family=Open+Sans:wght@400;600;700&display=swap" rel="stylesheet">
<style>
:root{
  --blue:#2b8fd8;
  --blue-dark:#1f6fae;
  --blue-deep:#2f6d9c;
  --ink:#2b2b2b;
  --text:#6b6b6b;
  --light:#f2f2f2;
  --line:#dddddd;
  --white:#ffffff;
  --dark:#1d1d1d;
  --grey-btn:#8c8c8c;
}
*{box-sizing:border-box;margin:0;padding:0}
html,body{width:1200px;height:3724px;overflow:hidden;background:var(--white)}
body{font-family:"Open Sans",Arial,sans-serif;color:var(--text);font-size:13px;line-height:1.6}
.page{position:relative;width:1200px;height:3724px;overflow:hidden}
.section{position:absolute;left:0;width:1200px}
h2,h3,.display{font-family:"Titillium Web",Arial,sans-serif}
.btn{display:inline-block;font-family:"Titillium Web",Arial,sans-serif;font-weight:600;font-size:14px;text-transform:uppercase;letter-spacing:.5px;padding:9px 26px;border-radius:3px}
.section-title{display:flex;flex-direction:column;align-items:center;gap:6px;color:var(--blue);font-size:28px;font-weight:600}
.section-title svg{width:26px;height:14px}

/* header */
.site-header{top:0;height:110px;background:var(--white);display:flex;align-items:center;justify-content:space-between;padding:0 40px}
.brand{display:flex;align-items:center;gap:10px;font-family:"Titillium Web",Arial,sans-serif;font-weight:700;font-size:26px;color:var(--blue)}
.brand-dot{width:16px;height:16px;background:var(--blue)}
.main-nav{display:flex;align-items:center;gap:22px;font-family:"Titillium Web",Arial,sans-serif;font-size:14px;font-weight:600;color:var(--ink);text-transform:uppercase}
.main-nav .btn{background:var(--blue);color:var(--white);padding:8px 18px;font-size:13px}

/* hero */
.hero{top:110px;height:490px;background:linear-gradient(180deg,#c9d6df 0%,#a5b8c5 35%,#6f7f86 60%,#4c4a42 80%,#3a3328 100%)}
.hero-copy{position:absolute;left:180px;top:300px;width:840px;text-align:center;color:var(--white);font-family:"Titillium Web",Arial,sans-serif;font-size:24px;font-weight:600;line-height:1.35;text-shadow:0 1px 3px rgba(0,0,0,.45)}
.hero .btn{position:absolute;left:525px;top:408px;border:2px solid var(--white);color:var(--white);background:rgba(0,0,0,.25)}

/* subscribe */
.subscribe{top:600px;height:135px;background:var(--blue);display:flex;align-items:center;padding:0 40px;gap:60px;color:var(--white)}
.subscribe-title{font-family:"Titillium Web",Arial,sans-serif;line-height:1}
.subscribe-title strong{display:block;font-size:50px;font-weight:700}
.subscribe-title span{display:block;font-size:28px;font-weight:600;margin-top:4px}
.subscribe-form{display:flex;gap:14px}
.field{width:310px;height:44px;background:var(--white);color:#888;font-size:14px;padding:11px 14px}
.subscribe-form .btn{background:var(--dark);color:var(--white);height:44px;padding:11px 22px}

/* about */
.about{top:735px;height:385px;text-align:center;padding-top:55px}
.about p{width:1060px;margin:26px auto 0;font-size:13px}
.about .btn,.learn-grey{background:var(--grey-btn);color:var(--white);margin-top:26px}

/* life coaching */
.coaching{top:1120px;height:370px;background:linear-gradient(90deg,#2e5f86 0%,#4d86b2 35%,#3a77a8 55%,#2d6a9c 100%)}
.coaching-copy{position:absolute;left:740px;top:70px;width:400px;color:var(--white)}
.coaching-copy h3{font-size:28px;font-weight:600;margin-bottom:10px}
.coaching-copy .btn{border:2px solid var(--white);color:var(--white);margin:28px 0 0 50px}

/* packages */
.packages{top:1500px;height:420px}
.packages .section-title{margin-top:20px}
.pkg-menu{position:absolute;left:50px;top:145px;width:210px}
.pkg-menu .item{border:1px solid var(--line);padding:10px 14px;font-size:13px;color:var(--ink);font-weight:600;background:var(--white)}
.pkg-menu .item.active{background:var(--blue-deep);color:var(--white);margin-top:16px;border-color:var(--blue-deep)}
.pkg-body{position:absolute;left:290px;top:110px;width:560px;font-size:12.5px}
.pkg-body .avail{margin-top:14px;color:var(--ink);font-weight:700}
.file-icons{display:flex;gap:16px;margin-top:8px}
.pkg-photo{position:absolute;left:890px;top:120px;width:250px;height:210px;background:linear-gradient(135deg,#f1ece6 0%,#e2d3c6 40%,#c8222c 55%,#b01e28 80%,#efe8e0 100%)}

/* books */
.books{top:1940px;height:410px;background:linear-gradient(180deg,#efefef,#e3e3e3)}
.books .section-title{margin-top:28px}
.book-row{position:absolute;left:210px;top:120px;width:780px;height:260px;display:flex;justify-content:space-between}
.book{position:relative;width:160px;height:230px;box-shadow:3px 4px 8px rgba(0,0,0,.3)}
.book.b1{background:linear-gradient(180deg,#2e2e2e,#1c4d6b 60%,#e59a2a)}
.book.b2{background:linear-gradient(180deg,#f5f5f5,#e2392b 60%,#c72d22)}
.book.b3{background:linear-gradient(180deg,#2a7fc8,#1c4f8d 70%,#173d6a)}
.book.b4{background:linear-gradient(180deg,#101a2a,#3b4b63 55%,#1d2a3b)}
.badge{position:absolute;left:-16px;top:-18px;width:58px;height:58px;border-radius:50%;background:var(--blue);color:var(--white);font-size:11px;font-weight:700;line-height:1.1;display:flex;align-items:center;justify-content:center;text-align:center;border:3px solid var(--white)}
.shelf{position:absolute;left:190px;top:352px;width:820px;height:14px;background:linear-gradient(180deg,#fafafa,#cfcfcf);box-shadow:0 4px 8px rgba(0,0,0,.2)}
.arrow{position:absolute;top:220px;width:30px;height:30px;border-radius:50%;background:#9a9a9a;display:flex;align-items:center;justify-content:center}
.arrow.left{left:140px}.arrow.right{left:1030px}

/* testimonials */
.testimonials{top:2400px;height:370px;background:linear-gradient(90deg,#2f73a8 0%,#3a86bd 55%,#5f9dc6 75%,#2f6e9e 100%)}
.testimonials .section-title{color:var(--white);margin-top:28px}
.avatar{position:absolute;left:90px;top:130px;width:130px;height:130px;border-radius:50%;background:radial-gradient(circle at 50% 45%,#e9d3c4,#b98e73);border:5px solid var(--white)}
.quote-body{position:absolute;left:270px;top:130px;width:870px;color:var(--white);font-size:13px}
.quote-mark{position:absolute;font-family:Georgia,serif;font-size:60px;line-height:1;color:var(--white)}
.author{position:absolute;left:290px;top:275px;color:var(--white);font-style:italic;font-size:14px}

/* news */
.news{top:2780px;height:440px}
.news .section-title{margin-top:22px}
.news-grid{position:absolute;left:100px;top:120px;width:1000px;display:flex;justify-content:space-between}
.news-card{width:310px}
.news-img{height:190px}
.n1{background:linear-gradient(180deg,#a9c0d2,#7c8a8c 60%,#4a4035)}
.n2{background:linear-gradient(180deg,#f3a548,#e56d2b 55%,#6b3820)}
.n3{background:linear-gradient(180deg,#9ab6cf,#8a7a63 60%,#5a4a38)}
.news-card h4{font-family:"Titillium Web",Arial,sans-serif;font-size:15px;font-weight:700;color:var(--ink);line-height:1.3;margin-top:16px}
.news-card p{font-size:12px;margin-top:8px}

/* footer */
.site-footer{top:3220px;height:460px;background:var(--light)}
.footer-brand{position:absolute;right:40px;top:14px;font-size:26px}
.footer-cols{position:absolute;left:50px;top:120px;width:1100px;display:flex;gap:60px}
.footer-cols h5{font-family:"Titillium Web",Arial,sans-serif;font-size:14px;font-weight:700;color:var(--ink);text-transform:uppercase;margin-bottom:12px}
.footer-cols ul{list-style:none;font-size:12.5px;line-height:1.9}
.col-links{width:180px}.col-shop{width:220px}.col-contact{width:300px}
.contact-line{display:flex;gap:10px;align-items:flex-start;font-size:12.5px;margin-bottom:10px}
.contact-line svg{flex:none;margin-top:3px}
.form-field{display:block;width:230px;height:32px;background:var(--white);border:1px solid var(--line);font-size:12px;color:#999;padding:6px 10px;margin-bottom:10px}
.form-field.tall{height:80px}
.footer-cols .btn{background:var(--dark);color:var(--white);font-size:12px;padding:6px 18px;margin-left:130px}
.bottom-bar{top:3680px;height:44px;background:var(--blue-dark);color:var(--white);display:flex;align-items:center;justify-content:space-between;padding:0 40px;font-size:11.5px;text-transform:uppercase}
.socials{display:flex;gap:8px}
.socials span{width:22px;height:22px;border-radius:50%;background:var(--white);opacity:.9}
</style>
</head>
<body>
<div class="page">

  <header class="section site-header">
    <div class="brand"><span class="brand-dot"></span>Vivid Horizon Mentors</div>
    <nav class="main-nav">
      <span>Home</span><span>About</span><span>Life Coaching</span><span>Packages</span><span>Books</span><span>Testimonials</span><span>News</span><span>Shop</span><span>Contact</span>
      <span class="btn">Subscribe Now</span>
    </nav>
  </header>

  <section class="section hero" role="img" aria-label="Photograph of a hiker standing on a rocky mountain peak above a misty valley">
    <p class="hero-copy">Vivid Horizon Mentors offers a team of coaches who can help people breakthrough the barriers that keep them from reaching their physical, spiritual, financial, leadership and relationship goals.</p>
    <span class="btn">Get Started</span>
  </section>

  <section class="section subscribe">
    <div class="subscribe-title"><strong>SUBSCRIBE</strong><span>AND GET STARTED</span></div>
    <div class="subscribe-form">
      <div class="field">Name</div>
      <div class="field">Email Address</div>
      <span class="btn">Sign Me Up</span>
    </div>
  </section>

  <section class="section about">
    <h2 class="section-title"><svg viewBox="0 0 26 14"><path d="M2 12 L13 3 L24 12" fill="none" stroke="currentColor" stroke-width="3"/></svg>About Vivid Horizon Mentors</h2>
    <p>Our mentors walk beside you as you set clear goals, build lasting habits and grow in body, mind and spirit. Each week brings fresh lessons, guided exercises and honest conversation to keep you moving. We believe every person carries untapped strength, and our work is to help you uncover it, shape it and put it to use in your home, your career and your community. Through video, audio and print material, you gain practical tools you can apply right away, along with a supportive circle of members who share their progress and cheer each other on toward the next level of success.</p>
    <span class="btn learn-grey">Learn More</span>
  </section>

  <section class="section coaching" role="img" aria-label="Photograph of a woman with arms stretched wide toward an open sky, tinted blue">
    <div class="coaching-copy">
      <h3>Life Coaching</h3>
      <p>One-on-one sessions help you name what holds you back and map the steps forward. Your coach listens, asks sharp questions and keeps you accountable as you build the life you want, one clear decision at a time, with steady support along the way.</p>
      <span class="btn">Learn More</span>
    </div>
  </section>

  <section class="section packages">
    <h2 class="section-title"><svg viewBox="0 0 26 14"><path d="M2 12 L13 3 L24 12" fill="none" stroke="currentColor" stroke-width="3"/></svg>Our Packages</h2>
    <div class="pkg-menu">
      <div class="item">Featured Package</div>
      <div class="item active">Show Past Subscribers</div>
    </div>
    <div class="pkg-body">
      <p>Every week a new package opens to members, bringing a focused theme with readings, recorded talks and short practice tasks. Work through it at your own pace, then join the discussion to share what changed for you and learn from others on the same path. Past packages stay available so you can revisit any lesson whenever you need a reminder of how far you have come.</p>
      <p class="avail">Available in :</p>
      <div class="file-icons">
        <svg width="30" height="36" viewBox="0 0 30 36"><path d="M2 2h18l8 8v24H2z" fill="none" stroke="#555" stroke-width="2"/><path d="M8 16h14M8 22h14M8 28h10" stroke="#555" stroke-width="2"/></svg>
        <svg width="30" height="36" viewBox="0 0 30 36"><path d="M2 2h18l8 8v24H2z" fill="none" stroke="#555" stroke-width="2"/><path d="M11 14v12l10-6z" fill="#555"/></svg>
        <svg width="30" height="36" viewBox="0 0 30 36"><path d="M2 2h18l8 8v24H2z" fill="none" stroke="#555" stroke-width="2"/><path d="M9 18h4l5-5v14l-5-5H9z" fill="#555"/></svg>
      </div>
    </div>
    <div class="pkg-photo" role="img" aria-label="Photograph of a red and white life coach sign"></div>
  </section>

  <section class="section books">
    <h2 class="section-title"><svg viewBox="0 0 26 14"><path d="M2 12 L13 3 L24 12" fill="none" stroke="currentColor" stroke-width="3"/></svg>Our Books</h2>
    <div class="arrow left"><svg width="12" height="12" viewBox="0 0 12 12"><path d="M8 1 L3 6 L8 11" fill="none" stroke="#fff" stroke-width="2"/></svg></div>
    <div class="book-row">
      <div class="book b1" role="img" aria-label="Book cover for a life coaching manual"><span class="badge">Learn More</span></div>
      <div class="book b2" role="img" aria-label="Book cover with a red life coach theme"><span class="badge">Learn More</span></div>
      <div class="book b3" role="img" aria-label="Blue book cover for a guide to life coaching"><span class="badge">Learn More</span></div>
      <div class="book b4" role="img" aria-label="Dark book cover on personal coaching"><span class="badge">Learn More</span></div>
    </div>
    <div class="shelf"></div>
    <div class="arrow right"><svg width="12" height="12" viewBox="0 0 12 12"><path d="M4 1 L9 6 L4 11" fill="none" stroke="#fff" stroke-width="2"/></svg></div>
  </section>

  <section class="section testimonials" role="img" aria-label="Photograph of a smiling coaching client, tinted blue">
    <h2 class="section-title"><svg viewBox="0 0 26 14"><path d="M2 12 L13 3 L24 12" fill="none" stroke="currentColor" stroke-width="3"/></svg>What They Say About Us</h2>
    <div class="avatar" role="img" aria-label="Portrait photo of the client"></div>
    <span class="quote-mark" style="left:240px;top:118px">&ldquo;</span>
    <p class="quote-body">Joining this program changed how I face each morning. My coach helped me see the patterns that kept me stuck and gave me simple steps to break them. The weekly packages kept me focused, and reading other members' stories reminded me I was never alone. Within a few months I had a new job, a healthier routine and a calmer mind. I now set goals with confidence and actually reach them. I recommend this team to anyone ready to grow.</p>
    <span class="quote-mark" style="left:1110px;top:220px">&rdquo;</span>
    <p class="author">Marisa Delcourt</p>
  </section>

  <section class="section news">
    <h2 class="section-title"><svg viewBox="0 0 26 14"><path d="M2 12 L13 3 L24 12" fill="none" stroke="currentColor" stroke-width="3"/></svg>Latest News</h2>
    <div class="news-grid">
      <article class="news-card">
        <div class="news-img n1" role="img" aria-label="Photograph of a climber on a mountain ridge"></div>
        <h4>News #1<br>January 16, 2016</h4>
        <p>Our spring program opens soon with new lessons on focus, energy and steady daily habits for lasting change.</p>
      </article>
      <article class="news-card">
        <div class="news-img n2" role="img" aria-label="Photograph of people jumping against a sunset sky"></div>
        <h4>News #2<br>January 8, 2016</h4>
        <p>Members gathered online to celebrate a year of growth, sharing stories of goals reached and fears overcome.</p>
      </article>
      <article class="news-card">
        <div class="news-img n3" role="img" aria-label="Photograph of a person celebrating on a hilltop"></div>
        <h4>News #3<br>January 2, 2016</h4>
        <p>A new audio series on leadership and relationships is now ready for every subscriber to enjoy this month.</p>
      </article>
    </div>
  </section>

  <footer class="section site-footer">
    <div class="brand footer-brand"><span class="brand-dot"></span>Vivid Horizon Mentors</div>
    <div class="footer-cols">
      <div class="col-links">
        <h5>Quick Links</h5>
        <ul><li>Home</li><li>Life Coaching</li><li>Packages</li><li>Books</li><li>Testimonials</li><li>Contact</li><li>Subscribe Now</li></ul>
      </div>
      <div class="col-shop">
        <h5>Shop</h5>
        <ul><li>Merchandise</li><li>My Account</li><li>Shipping &amp; Returns</li><li>FAQ</li></ul>
      </div>
      <div class="col-contact">
        <h5>Contact</h5>
        <div class="contact-line"><svg width="12" height="16" viewBox="0 0 12 16"><path d="M6 1a5 5 0 0 1 5 5c0 4-5 9-5 9S1 10 1 6a5 5 0 0 1 5-5z" fill="#777"/><circle cx="6" cy="6" r="2" fill="#f2f2f2"/></svg><span>Vivid Horizon Mentors<br>48 Lakeview Avenue<br>Harbor Point, CA 90000</span></div>
        <div class="contact-line"><svg width="14" height="14" viewBox="0 0 14 14"><path d="M3 1l3 3-2 2c1 2 2 3 4 4l2-2 3 3-2 3C5 14 0 9 0 3z" fill="#777"/></svg><span>(555) 284-7710</span></div>
        <div class="contact-line"><svg width="14" height="12" viewBox="0 0 14 12"><rect x="1" y="1" width="12" height="10" fill="none" stroke="#777" stroke-width="1.5"/><path d="M1 1l6 5 6-5" fill="none" stroke="#777" stroke-width="1.5"/></svg><span>hello@vividhorizonmentors.example</span></div>
      </div>
      <div class="col-form">
        <h5>Send Us A Message</h5>
        <span class="form-field">Name</span>
        <span class="form-field">Email</span>
        <span class="form-field tall">Message</span>
        <span class="btn">Submit</span>
      </div>
    </div>
  </footer>

  <div class="section bottom-bar">
    <span>Copyright &copy; 2016 Vivid Horizon Mentors. All rights reserved.</span>
    <div class="socials"><span></span><span></span><span></span></div>
  </div>

</div>
</body>
</html>
```